Awesome Business Card Design needed!

Hey there.
I'm looking for a simple but awesome business card design.
Type of company: Online advertisement agency
(please don't use the typical business people or statistics images on the card)
The front has to display the business name
and possibly some sort of logo ( perhaps something with the two M's of the biz name )
And the back of the card should say:
Name
Phone
Email
Let your imagination flow.
here are some designs that I like and that you can use as inspiration.
Simple but Awesome
http://images.pixelvantor.net/designs/55128_877673_43091_thumbnail.jpg
http://images.pixelvantor.net/designs/37714_747642_40106_image.jpg
http://images.pixelvantor.net/designs/55128_877673_43091_image.jpg
http://images.pixelvantor.net/designs/51321_781878_43091_image.jpg
http://images.pixelvantor.net/designs/33378_399063_15912_image.jpg
http://images.pixelvantor.net/designs/2337_271604_9495_image.jpg
good luck

```html
<!DOCTYPE html>
<html lang="en">
<head>
<meta charset="utf-8">
<title>Velstra Media – Business Card</title>
<link rel="stylesheet" href="https://fonts.googleapis.com/css2?family=Open+Sans:wght@400&display=swap">
<style>
  :root {
    --backdrop: #e8e8e8;
    --card: #ffffff;
    --ink: #1a1a1a;
    --band: #111111;
    --band-text: #ffffff;
  }
  html, body {
    margin: 0;
    padding: 0;
    width: 1200px;
    height: 900px;
    overflow: hidden;
    background: var(--backdrop);
    font-family: "Open Sans", sans-serif;
  }
  .canvas {
    position: relative;
    width: 1200px;
    height: 900px;
  }
  .card {
    position: absolute;
    left: 80px;
    top: 122px;
    width: 1040px;
    height: 655px;
    background: var(--card);
    box-shadow: 0 2px 10px rgba(0, 0, 0, 0.08);
  }
  .company-name {
    position: absolute;
    left: 50px;
    top: 265px;
    margin: 0;
    font-size: 55px;
    font-weight: 400;
    line-height: 1;
    color: var(--ink);
    white-space: nowrap;
  }
  .tagline-band {
    position: absolute;
    left: 435px;
    right: 0;
    top: 298px;
    height: 28px;
    background: var(--band);
  }
  .tagline {
    position: absolute;
    left: 20px;
    top: 0;
    margin: 0;
    font-size: 21px;
    line-height: 28px;
    color: var(--band-text);
    letter-spacing: 0.3px;
    white-space: nowrap;
  }
  .contact {
    position: absolute;
    left: 455px;
    top: 340px;
    margin: 0;
    padding: 0;
    list-style: none;
    font-size: 24px;
    line-height: 40px;
    color: var(--ink);
  }
</style>
</head>
<body>
  <main class="canvas">
    <section class="card">
      <h1 class="company-name">Velstra Media</h1>
      <div class="tagline-band">
        <p class="tagline">ONLINE ADVERTISEMENT AGENCY</p>
      </div>
      <ul class="contact">
        <li class="contact-name">Daniel Velstra</li>
        <li class="contact-phone">0987 6543 2109</li>
        <li class="contact-web">velstramedia.com</li>
      </ul>
    </section>
  </main>
</body>
</html>
```